New Fresh design for online Rabbit Game

Hi,

we are a french company working on a online rabbits game for kids, and not kids.

Our website is www.trovelu.fr, but you can look at the US version : www.hoplark.com

We buy our actual design 2 years ago, but we now think it's too boring and washed out...

We need yours talent to make a really more exacting, more colorful, fresh and dynamic design.

In our game, players have to breed and train rabbits and to make them run races. Players run again friends or players.

Players are kids, between 8 and 15 years. But best players are often parents of these kids !

Our ambiance is clearly funny. We really like if color theme or background look like a nice blue sky, and / or beach. Something that make people happy to come, and say "You are here on holly days to have fun !"

I think the best is if we have 2 layouts, one for the Home page, and one for all other page.

For home page, we are really open to any proposition, we just need to keep our features :
- registration (with rabbit preview)
- connection
- game preview (images slide with small text)
- live race preview (as we have actually)

For other pages layout, we need a layout with a standard container (maybe 850 px width?), and our 2 navigation's bar.

We only need psd, no html integration.

Thanks for your help, please ask me for any questions.
Updates

Hi, 

I have just added some information, concerning layout.

Also we have just committed the budget.

Target Market(s)

Mostly kids between 8 and 15 years.

Industry/Entity Type

It Company

Requirements
Must have
• We already have some characters, like Mr Pebblo at the home page and our rabbits. We want to keep all of them, so new design have to match with there style (carton).

If you create an account, you will see we have a big nav bar with 6 tabs, and a little top bar. We absolutely need them to keep a easy navigation in website.

We also need some proposition of element style, like h1, h2, h3, hr, inputs, buttons, notification bubble, etc... So we can work to improve all our pages.
Nice to have
• I think the actual website is a little to wide (about 1000px width). Maybe something like 900px - 850px is more elegant ?
In this case, we can arrange pages to deal with it.

It can be cool if major colors are stil blue and green, to match a little with actual colors. But it's no very important.
Should not have
• We don't want too big header picture (for the all pages layout). I mean, players have to focus on the content.

We don't want photo realistic style, our style is cartoon.

We don't want flash. But Js animations are ok.

```html
<!DOCTYPE html>
<html lang="en">
<head>
<meta charset="utf-8">
<title>Lopsprint – Forum Homepage</title>
<link rel="stylesheet" href="https://fonts.googleapis.com/css2?family=Kaushan+Script&family=Nunito:wght@600;700;800&family=Abel&display=swap">
<style>
  :root {
    --sky-top: #9fdcf0;
    --sky-bottom: #b9e8f6;
    --sand: #f0c85a;
    --sand-dark: #e2b444;
    --panel-top: #cfe9a4;
    --panel-bottom: #a7e27e;
    --lime: #c7e36a;
    --ribbon: #4fb3d8;
    --ribbon-dark: #2f8fb8;
    --ribbon-light: #8fd3ec;
    --title-box: #3aa3c7;
    --white: #ffffff;
    --nav-active: #cbe86a;
    --card: #e9878c;
    --card-hover: #f2b8ba;
    --card-border: #d4565d;
    --card-meta: #9c2a30;
    --brand-pink: #e26f86;
    --footer-text: #3d4a2c;
    --button-top: #a6dc84;
    --button-bottom: #6cbb55;
    --text-dark: #2e3a26;
  }
  html, body { margin: 0; padding: 0; overflow: hidden; }
  body { width: 1200px; height: 1038px; background: var(--sky-bottom); }
  .canvas {
    position: relative; width: 1200px; height: 1038px; overflow: hidden;
    background: linear-gradient(180deg, var(--sky-top) 0%, var(--sky-bottom) 100%);
    font-family: "Nunito", sans-serif;
  }
  .abs { position: absolute; }

  /* beach */
  .beach { left: 0; top: 990px; width: 1200px; height: 48px;
    background: linear-gradient(180deg, var(--sand) 0%, var(--sand-dark) 100%); }
  .beach-toys { left: 59px; top: 975px; width: 72px; height: 50px; border-radius: 14px;
    background: linear-gradient(135deg, #f3a05a, #e5533b); }
  .beach-shells { left: 910px; top: 1000px; width: 57px; height: 22px; border-radius: 11px;
    background: linear-gradient(90deg, #c9a58a, #e6d2c0); }
  .beach-umbrella { left: 1087px; top: 940px; width: 87px; height: 80px; border-radius: 40px 40px 10px 10px;
    background: linear-gradient(180deg, #7cc860 0%, #e9f4d8 55%, #d9584a 100%); }
  .copyright { left: 0; width: 1258px; top: 1005px; text-align: center;
    font-family: "Abel", sans-serif; font-size: 16px; color: #3a2e12; }

  /* brand plate */
  .brand-plate { left: 373px; top: 26px; width: 440px; height: 90px; border-radius: 16px 16px 0 0;
    background: linear-gradient(180deg, #d6ec84, var(--lime)); box-shadow: 0 2px 4px rgba(0,0,0,.15); }
  .brand-name { position: absolute; left: 0; right: 0; top: 16px; text-align: center;
    font-family: "Nunito", sans-serif; font-weight: 800; font-size: 48px; color: var(--brand-pink); }
  .brand-mascot { position: absolute; top: 6px; width: 56px; height: 76px; border-radius: 20px;
    background: linear-gradient(180deg, #e8d9b8, #c9b58e); }
  .brand-mascot.left { left: 10px; }
  .brand-mascot.right { right: 10px; background: linear-gradient(180deg, #f3b25a, #dc8a34); }

  /* main panel */
  .panel { left: 183px; top: 109px; width: 812px; height: 782px; border-radius: 10px;
    background: linear-gradient(180deg, var(--panel-top) 0%, var(--panel-bottom) 100%);
    box-shadow: 0 4px 6px rgba(40,80,30,.35); }
  .panel-header { left: 183px; top: 187px; width: 812px; height: 115px; background: #b9de84; }
  .panel-zigzag { left: 183px; top: 296px; }

  /* nav ribbon */
  .ribbon-tails { left: 105px; top: 158px; }
  .nav-bar { left: 164px; top: 131px; width: 853px; height: 56px;
    background: linear-gradient(180deg, var(--ribbon-light) 0%, var(--ribbon) 40%, var(--ribbon-dark) 100%);
    box-shadow: 0 3px 5px rgba(0,0,0,.25); display: flex; justify-content: center; align-items: center; gap: 24px; }
  .nav-item { font-family: "Kaushan Script", cursive; font-size: 30px; color: var(--white);
    text-shadow: 0 2px 2px rgba(20,60,90,.5); }
  .nav-item.active { color: var(--nav-active); }
  .nav-sep { color: var(--white); font-size: 18px; }

  /* page title + search */
  .page-title { left: 211px; top: 226px; width: 334px; height: 52px; margin: 0; background: var(--title-box);
    display: flex; align-items: center; justify-content: center;
    font-family: "Kaushan Script", cursive; font-weight: 400; font-size: 28px; color: var(--white); }
  .search-field { left: 623px; top: 244px; width: 206px; height: 33px; border-radius: 17px;
    background: #e7f5cf; box-shadow: inset 0 1px 3px rgba(0,0,0,.25);
    display: flex; align-items: center; gap: 6px; padding-left: 12px; box-sizing: border-box;
    font-size: 15px; font-weight: 700; color: #4c5a3c; }
  .search-button { left: 838px; top: 240px; width: 96px; height: 33px; border-radius: 17px;
    background: linear-gradient(180deg, var(--button-top), var(--button-bottom));
    box-shadow: 0 2px 3px rgba(0,0,0,.3); display: flex; align-items: center; justify-content: center;
    font-size: 15px; font-weight: 700; color: var(--text-dark); }
  .search-mascot { left: 862px; top: 213px; width: 50px; height: 27px; border-radius: 14px;
    background: linear-gradient(180deg, #f1a64a, #d87f2a); }

  /* forum list */
  .forum-list { left: 244px; top: 334px; width: 684px; display: flex; flex-direction: column; gap: 14px; }
  .forum-card { position: relative; height: 88px; box-sizing: border-box; background: var(--card);
    border: 4px solid var(--card-border); padding: 14px 14px 0 16px; color: var(--white); }
  .forum-card.is-hover { background: var(--card-hover); }
  .forum-title { font-size: 29px; font-weight: 700; line-height: 1; }
  .forum-desc { margin-top: 11px; font-size: 15px; font-weight: 700; }
  .forum-meta { position: absolute; right: 12px; top: 20px; text-align: right;
    font-size: 17px; font-weight: 700; color: var(--card-meta); line-height: 17px; }

  /* footer */
  .footer { left: 183px; top: 916px; width: 812px; height: 51px; box-sizing: border-box;
    background: linear-gradient(180deg, #c9ec9c, #aee485); box-shadow: 0 3px 4px rgba(0,0,0,.25);
    display: flex; align-items: center; padding: 0 20px 0 10px;
    font-family: "Abel", sans-serif; font-size: 19px; color: var(--footer-text); }
  .partner-badge { width: 101px; height: 31px; background: #2c6aa8; margin-left: 24px; }
  .footer-links { margin-left: auto; }
</style>
</head>
<body>
<div class="canvas">

  <div class="abs beach"></div>
  <div class="abs beach-toys" role="img" aria-label="Beach ball and sand bucket illustration"></div>
  <div class="abs beach-shells" role="img" aria-label="Seashells illustration"></div>
  <div class="abs beach-umbrella" role="img" aria-label="Beach umbrella and deck chair illustration"></div>
  <div class="abs copyright">copyrights</div>

  <div class="abs brand-plate">
    <div class="brand-mascot left" role="img" aria-label="Cartoon rabbit character"></div>
    <div class="brand-name">Lopsprint</div>
    <div class="brand-mascot right" role="img" aria-label="Cartoon rabbit character"></div>
  </div>

  <div class="abs panel"></div>
  <div class="abs panel-header"></div>
  <svg class="abs panel-zigzag" width="812" height="10" viewBox="0 0 812 10">
    <defs>
      <pattern id="zigzag" width="8" height="10" patternUnits="userSpaceOnUse">
        <polygon fill="#b9de84" points="0,0 8,0 8,4 4,8 0,4"/>
      </pattern>
    </defs>
    <rect width="812" height="10" fill="url(#zigzag)"/>
  </svg>

  <svg class="abs ribbon-tails" width="967" height="72" viewBox="0 0 967 72">
    <polygon fill="#2f8fb8" points="0,12 59,0 59,44 62,72 20,46 40,30"/>
    <polygon fill="#2f8fb8" points="967,12 908,0 908,44 905,72 947,46 927,30"/>
  </svg>
  <nav class="abs nav-bar">
    <span class="nav-item">Home</span><span class="nav-sep">·</span>
    <span class="nav-item">News</span><span class="nav-sep">·</span>
    <span class="nav-item active">Forum</span><span class="nav-sep">·</span>
    <span class="nav-item">Records</span>
  </nav>

  <h1 class="abs page-title">Forum Homepage</h1>
  <div class="abs search-mascot" role="img" aria-label="Sleeping cartoon rabbit"></div>
  <div class="abs search-field">
    <svg width="14" height="14" viewBox="0 0 14 14"><circle cx="6" cy="6" r="4.5" fill="none" stroke="#4c5a3c" stroke-width="1.8"/><line x1="9.3" y1="9.3" x2="13" y2="13" stroke="#4c5a3c" stroke-width="1.8"/></svg>
    <span>search...</span>
  </div>
  <div class="abs search-button">Search</div>

  <div class="abs forum-list">
    <div class="forum-card">
      <div class="forum-title">General discussion</div>
      <div class="forum-desc">Discuss about Lopsprint</div>
      <div class="forum-meta">504topics - 13131 messages<br>modified 1 hour ago</div>
    </div>
    <div class="forum-card is-hover">
      <div class="forum-title">In game help</div>
      <div class="forum-desc">You have question? Somebody certainly have the answer!</div>
      <div class="forum-meta">504topics - 13131 messages<br>modified 1 hour ago</div>
    </div>
    <div class="forum-card">
      <div class="forum-title">Playgrounds</div>
      <div class="forum-desc">Role playing</div>
      <div class="forum-meta">504topics - 13131 messages<br>modified 1 hour ago</div>
    </div>
    <div class="forum-card">
      <div class="forum-title">Translation errors</div>
      <div class="forum-desc">You have found an incorrect sentence? You can help!</div>
      <div class="forum-meta">504topics - 13131 messages<br>modified 1 hour ago</div>
    </div>
    <div class="forum-card">
      <div class="forum-title">Bugs and technical problems</div>
      <div class="forum-desc">You think something is going wrong?</div>
      <div class="forum-meta">504topics - 13131 messages<br>modified 1 hour ago</div>
    </div>
  </div>

  <footer class="abs footer">
    <span>Partners:</span>
    <span class="partner-badge" role="img" aria-label="Partner listing badge"></span>
    <span class="footer-links">Rules - General Terms and Conditions - Contact - Lopsprint.com 3.0</span>
  </footer>

</div>
</body>
</html>
```